Floor Inspections and Consulting

We provide inspections and consulting services on various floor coverings, e.g. carpet, hardwood, etc. We also do expert witness work for attorneys due to floor covering failures. We current have a logo, just need it incorporated into a new design. I have examples of cards I have found on the internet that capture my attention and make a statement. I have included our original business card, which in my opinion is terrible, but it does have our logo on it.

```html
<!DOCTYPE html>
<html lang="en">
<head>
<meta charset="utf-8">
<title>Keystone Flooring Inspections – Business Card</title>
<link rel="stylesheet" href="https://fonts.googleapis.com/css2?family=Montserrat:wght@500;600;700&family=Roboto:wght@500&display=swap">
<style>
  :root {
    --backdrop: #2e2e2e;
    --card: #161616;
    --orange: #e8700a;
    --light: #e6e6e6;
    --grey: #8a8a8a;
  }
  * { margin: 0; padding: 0; box-sizing: border-box; }
  html, body { width: 1200px; height: 866px; overflow: hidden; }
  body {
    background: var(--backdrop);
    display: flex;
    align-items: center;
    justify-content: center;
    gap: 40px;
    font-family: "Montserrat", sans-serif;
  }
  .card {
    position: relative;
    width: 540px;
    height: 310px;
    background: var(--card);
    box-shadow: 0 14px 30px rgba(0,0,0,0.45);
    overflow: hidden;
  }
  .rule {
    position: absolute;
    height: 2px;
    background: var(--orange);
  }
  .brand {
    position: absolute;
    display: flex;
    align-items: center;
    gap: 12px;
    color: var(--orange);
    font-weight: 700;
    text-transform: uppercase;
    letter-spacing: 1px;
  }
  .brand-dot {
    flex: none;
    border-radius: 50%;
    background: var(--orange);
  }

  /* Contact side */
  .card-front .brand { left: 150px; top: 62px; font-size: 15px; }
  .card-front .brand-dot { width: 22px; height: 22px; }
  .card-front .rule-top { left: 70px; right: 30px; top: 110px; }
  .card-front .rule-bottom { left: 30px; width: 380px; bottom: 48px; }
  .person-name {
    position: absolute;
    left: 120px; top: 124px;
    color: var(--orange);
    font-weight: 700;
    font-size: 22px;
    letter-spacing: 2px;
    text-transform: uppercase;
  }
  .contact-list {
    position: absolute;
    left: 120px; top: 166px;
    list-style: none;
    color: var(--light);
    font-weight: 600;
    font-size: 14px;
    line-height: 22px;
    letter-spacing: 0.8px;
  }

  /* Company side */
  .card-back .brand {
    left: 70px; top: 78px;
    font-size: 27px;
    line-height: 32px;
    letter-spacing: 2px;
  }
  .card-back .brand-dot { width: 30px; height: 30px; }
  .card-back .rule-top { left: 40px; width: 230px; top: 64px; }
  .card-back .rule-bottom { right: 30px; width: 260px; top: 158px; }
  .service-line {
    position: absolute;
    left: 112px; top: 168px;
    color: var(--grey);
    font-weight: 600;
    font-size: 11px;
    letter-spacing: 2.5px;
    text-transform: uppercase;
  }
  .tagline {
    position: absolute;
    left: 70px; top: 200px;
    color: var(--grey);
    font-family: "Roboto", sans-serif;
    font-weight: 500;
    font-size: 16px;
  }
</style>
</head>
<body>
  <section class="card card-front" aria-label="Business card, contact side">
    <div class="brand"><span class="brand-dot"></span>Keystone Flooring Inspections</div>
    <div class="rule rule-top"></div>
    <h1 class="person-name">Daniel Marlow</h1>
    <ul class="contact-list">
      <li>555-214-7300</li>
      <li>daniel@keystonefloor.com</li>
      <li>www.keystonefloor.com</li>
    </ul>
    <div class="rule rule-bottom"></div>
  </section>

  <section class="card card-back" aria-label="Business card, company side">
    <div class="rule rule-top"></div>
    <div class="brand"><span class="brand-dot"></span><span>Keystone Flooring<br>Inspections</span></div>
    <div class="rule rule-bottom"></div>
    <p class="service-line">Analysis &amp; Consulting</p>
    <p class="tagline">Certified Floor Covering Inspection &amp; Consulting</p>
  </section>
</body>
</html>
```